5x7 Outpour Promotional Card For a Church Conference

We need a 5x7 promotional card design for a church conference called Harvest Lantern Gathering with the theme "Outpour" The pictures and files are attached. We are open to original ideas. Fonts are from Microsoft Word and definitely are open for change. The attached files are just a suggestion. Let your creative ideas flow. The website of hlgathering.org must be listed on both sides. The pictures should not be photo shopped.
Updates

Industry/Entity Type

Church

Colors
3176b5
0293ce
33a6d7
85cae6
85acd3

Requirements
Nice to have
• Would be great to have the word "OUTPOUR" in a font that looks like it is dripping in water.
Should not have
• should not be whimsical or playful

```html
<!DOCTYPE html>
<html lang="en">
<head>
<meta charset="utf-8">
<title>Harvest Lantern Gathering 2015 – Outpour Card</title>
<link href="https://fonts.googleapis.com/css2?family=Open+Sans:wght@400;700&family=PT+Sans+Narrow:wght@400;700&family=Great+Vibes&family=Cormorant+Garamond:ital,wght@1,500&display=swap" rel="stylesheet">
<style>
  :root {
    --page: #ffffff;
    --white: #ffffff;
    --navy: #2b3990;
    --speaker-blue: #2f6fb5;
    --web-blue: #1fa3dc;
    --ink: #1d1d1d;
    --frame: #9a9a9a;
    --sky-top: #6e6aa8;
    --sunset: #f09a3a;
    --glow: #f6d27a;
    --field: #a9a24a;
    --grass: #4f7f2c;
    --cliff: #5b4a36;
    --falls-dark: #3d4a4e;
    --mist: #c9d3d6;
  }
  * { margin: 0; padding: 0; box-sizing: border-box; }
  html, body { width: 873px; height: 1200px; overflow: hidden; background: var(--page); }
  .canvas { position: relative; width: 873px; height: 1200px; }

  .card { position: absolute; left: 55px; width: 759px; overflow: hidden; }
  .card--front { top: 37px; height: 543px; }
  .card--back { top: 616px; height: 542px; border: 1px solid var(--frame); background: var(--white); }

  .photo { position: absolute; inset: 0; }
  .photo--landscape {
    background:
      radial-gradient(ellipse 260px 120px at 170px 270px, var(--glow) 0%, rgba(246,210,122,0) 100%),
      linear-gradient(90deg, rgba(0,0,0,0) 0%, rgba(0,0,0,0) 62%, var(--cliff) 78%, #3e3326 100%),
      linear-gradient(180deg, var(--sky-top) 0%, #b07b7a 22%, var(--sunset) 42%, #e6b15a 56%, var(--field) 64%, var(--grass) 82%, #2f5a22 100%);
  }
  .photo--falls {
    bottom: auto; height: 240px;
    background:
      linear-gradient(180deg, rgba(255,255,255,0) 55%, var(--white) 100%),
      linear-gradient(90deg, #3a3a2e 0%, var(--falls-dark) 10%, #a9b5b8 30%, var(--mist) 50%, #8e9a9c 75%, #4a4438 100%);
  }

  .text { position: absolute; white-space: nowrap; }
  .brand { font-family: 'Open Sans', sans-serif; font-weight: 700; color: var(--white); letter-spacing: 0.5px; }
  .headline { font-family: 'Open Sans', sans-serif; font-weight: 700; color: var(--white); line-height: 1; }
  .year { font-family: 'Cormorant Garamond', serif; font-style: italic; font-weight: 500; }
  .theme { font-family: 'Great Vibes', cursive; color: var(--white); line-height: 1; }
  .dates { font-family: 'Open Sans', sans-serif; font-weight: 700; color: var(--white); }
  .site { font-family: 'PT Sans Narrow', sans-serif; font-weight: 700; }

  /* front */
  .card--front .brand { left: 50%; top: 40px; transform: translateX(-50%); font-size: 31px; font-family: 'PT Sans Narrow', sans-serif; }
  .card--front .headline--one { left: 33px; top: 116px; font-size: 49px; }
  .card--front .headline--two { left: 73px; top: 160px; font-size: 49px; }
  .card--front .headline--two .year { font-size: 58px; }
  .card--front .theme { left: 66px; top: 382px; font-size: 104px; }
  .card--front .dates { left: 208px; top: 472px; font-size: 22px; }
  .card--front .site { right: 16px; top: 510px; font-size: 28px; color: var(--white); }

  /* back */
  .card--back .brand { left: 88px; top: 195px; transform: translateY(-50%); font-size: 31px; font-family: 'PT Sans Narrow', sans-serif; }
  .card--back .headline--one { left: 354px; top: 55px; font-size: 30px; }
  .card--back .headline--two { left: 382px; top: 86px; font-size: 30px; }
  .card--back .headline--two .year { font-size: 36px; }
  .card--back .theme { left: 478px; top: 112px; font-size: 62px; }

  .speaker { position: absolute; top: 224px; width: 200px; text-align: center; transform: translateX(-50%); }
  .speaker__portrait { width: 103px; height: 103px; margin: 0 auto 13px; background: linear-gradient(160deg, #6c6c6c, #2a2a2a); }
  .speaker--two .speaker__portrait { background: linear-gradient(160deg, #8a7a68, #3a3430); }
  .speaker--three .speaker__portrait { background: linear-gradient(160deg, #7d6fc2, #2c2a4a); }
  .speaker__name { font-family: 'PT Sans Narrow', sans-serif; font-weight: 700; font-size: 17px; color: var(--speaker-blue); line-height: 1.05; }
  .speaker__date { font-family: 'PT Sans Narrow', sans-serif; font-size: 16px; color: var(--ink); line-height: 1.1; }
  .speaker--one { left: 179px; }
  .speaker--two { left: 380px; }
  .speaker--three { left: 573px; }

  .event { position: absolute; top: 397px; width: 320px; text-align: center; transform: translateX(-50%); }
  .event__title { font-family: 'PT Sans Narrow', sans-serif; font-weight: 700; font-size: 20px; color: var(--navy); line-height: 1.2; }
  .event__line { font-family: 'Open Sans', sans-serif; font-size: 16px; color: var(--ink); line-height: 1.45; }
  .event--prayer { left: 231px; }
  .event--services { left: 549px; }

  .card--back .site { left: 50%; top: 500px; transform: translateX(-50%); font-size: 28px; color: var(--web-blue); }
</style>
</head>
<body>
<div class="canvas">

  <section class="card card--front">
    <div class="photo photo--landscape" role="img" aria-label="Photograph of a tall waterfall pouring off a green cliff beside open fields under a glowing sunset sky"></div>
    <div class="text brand">HARVEST</div>
    <div class="text headline headline--one">LANTERN</div>
    <div class="text headline headline--two">GATHERING <span class="year">2015</span></div>
    <div class="text theme">Outpour!</div>
    <div class="text dates">August 25-28</div>
    <div class="text site">hlgathering.org</div>
  </section>

  <section class="card card--back">
    <div class="photo photo--falls" role="img" aria-label="Photograph of a wide misty waterfall between dark cliffs, fading into white"></div>
    <div class="text brand">HARVEST</div>
    <div class="text headline headline--one">LANTERN</div>
    <div class="text headline headline--two">GATHERING <span class="year">2015</span></div>
    <div class="text theme">Outpour!</div>

    <div class="speaker speaker--one">
      <div class="speaker__portrait" role="img" aria-label="Portrait photo of Evangelist Marian Cole"></div>
      <div class="speaker__name">Evangelist Marian Cole</div>
      <div class="speaker__date">Wednesday, August 26</div>
    </div>
    <div class="speaker speaker--two">
      <div class="speaker__portrait" role="img" aria-label="Portrait photo of Pastor Devon Hale"></div>
      <div class="speaker__name">Pastor Devon Hale</div>
      <div class="speaker__date">Thursday, August 27</div>
    </div>
    <div class="speaker speaker--three">
      <div class="speaker__portrait" role="img" aria-label="Portrait photo of Pastor Curtis Vance"></div>
      <div class="speaker__name">Pastor Curtis Vance</div>
      <div class="speaker__date">Friday, August 28</div>
    </div>

    <div class="event event--prayer">
      <div class="event__title">Community Prayer Service</div>
      <div class="event__line">Tuesday, August 25 at 7pm</div>
      <div class="event__line">Cornerstone Tabernacle</div>
      <div class="event__line">1480 Linden Ave, Fairview</div>
    </div>
    <div class="event event--services">
      <div class="event__title">Services</div>
      <div class="event__line">Wednesday-Friday at 7:30pm</div>
      <div class="event__line">Riverside Fellowship Church</div>
      <div class="event__line">3172 North Maple Ave, Brookdale</div>
    </div>

    <div class="text site">hlgathering.org</div>
  </section>

</div>
</body>
</html>
```